"Thank You" card for professional property management agency.

We need to create a DL size "Thank You" card primarily used to thank new clients for their business and referrals.
We are a real estate agency based on Sydney's Northern Beaches. We want the card to feel happy and professional, incorporating our logo.
See our website for details about our business - www.harbourlanerealty.com.au
We have attached our logo in black text and white text as well as some images we have used across our website.
One side must have the ability to hand write a message of thank you on.
I would like this to be a clean and simple design, feel free to use any image supplied, but we are also happy with plain or patterned designs too.

Target Market(s)

Property investors male and female aged 30-60

Industry/Entity Type

Real Estate

Font styles to use
Other font styles liked:
• Please let the designer choose font

Colors

Designer to choose colors to be used in the design.

Requirements
Must have
• DL Size: Full Bleed 213x102mm. Doc size 210x99mm (horizontal)
• Harbour Lane Realty Logo
• Contact Details:
• info@harbourlanerealty.com.au
• Tel: 0493 716 258
• Suite 3, 17 Wentmore Rd, Calderwood NSW 2417
• "Thank You" somewhere on the card
• Area or side to write message on.
• Design to be provided in editable photoshop PSD file and print ready PDF file
Nice to have
• Sleek professional design that feels "happy or grateful" as it is a thank you card
• Happy to use a plain colour or pattern on one side - it does not have to be an image provided, but feel free to design with either.
Should not have
• should not be too busy, keep it clean and simple.

```html
<!DOCTYPE html>
<html lang="en">
<head>
<meta charset="utf-8">
<title>Harbour Lane Realty – Thank You Card</title>
<link href="https://fonts.googleapis.com/css2?family=Montserrat:wght@400;500;600&display=swap" rel="stylesheet">
<style>
  :root {
    --page-bg: #e6e6e6;
    --card-charcoal: #3b3b3e;
    --accent-teal: #2ea3b5;
    --ring-white: #ffffff;
    --logo-white: #ffffff;
  }
  html, body {
    margin: 0;
    width: 1200px;
    height: 884px;
    overflow: hidden;
    background: var(--page-bg);
    font-family: "Montserrat", Arial, sans-serif;
  }
  .card {
    position: absolute;
    left: 50px;
    top: 182px;
    width: 1100px;
    height: 520px;
    background: var(--card-charcoal);
    overflow: hidden;
    box-shadow: 0 6px 22px rgba(0,0,0,0.18);
  }
  .hero-photo {
    position: absolute;
    left: 0; top: 0;
    width: 100%;
    height: 190px;
    background: linear-gradient(180deg, #8fc3e6 0%, #cfe3ef 45%, #9aa7a8 70%, #4f6b4a 100%);
  }
  .round-photo {
    position: absolute;
    border: 8px solid var(--ring-white);
    border-radius: 50%;
    box-shadow: 0 3px 10px rgba(0,0,0,0.35);
  }
  .round-photo.beach {
    left: 160px; top: 136px; width: 124px; height: 124px;
    background: linear-gradient(180deg, #7db6dc 0%, #3f7fa8 55%, #d9c9a4 100%);
  }
  .round-photo.harbour-tree {
    left: 322px; top: 120px; width: 164px; height: 164px;
    background: radial-gradient(circle at 45% 35%, #5f6a3a 0%, #4a5632 40%, #9db6c2 75%, #c9b68f 100%);
  }
  .round-photo.bay {
    left: 540px; top: 70px; width: 124px; height: 124px;
    background: linear-gradient(180deg, #9cc9ea 0%, #5b9bc6 50%, #2d6a92 100%);
  }
  .brand {
    position: absolute;
    left: 740px;
    top: 262px;
    display: flex;
    align-items: center;
    gap: 12px;
    white-space: nowrap;
    color: var(--logo-white);
    font-weight: 500;
    font-size: 22px;
    letter-spacing: 1px;
    text-transform: uppercase;
  }
  .brand-dot {
    width: 12px; height: 12px;
    border-radius: 50%;
    background: var(--logo-white);
  }
  .message {
    position: absolute;
    left: 56px;
    top: 356px;
    color: var(--accent-teal);
  }
  .message h1 {
    margin: 0 0 8px;
    font-size: 58px;
    font-weight: 600;
    letter-spacing: 2px;
    line-height: 1;
  }
  .contact {
    margin: 0;
    font-size: 19px;
    font-weight: 500;
    line-height: 1.35;
  }
</style>
</head>
<body>
  <section class="card">
    <div class="hero-photo" role="img" aria-label="Photo of modern waterfront homes under a blue sky"></div>
    <div class="round-photo beach" role="img" aria-label="Photo of a Northern Beaches beach and ocean"></div>
    <div class="round-photo harbour-tree" role="img" aria-label="Photo of a tree overlooking a harbour beach"></div>
    <div class="round-photo bay" role="img" aria-label="Photo of boats moored in a bay"></div>

    <div class="brand"><span class="brand-dot"></span>Harbour Lane Realty</div>

    <div class="message">
      <h1>THANK YOU</h1>
      <p class="contact">Suite 3, 17 Wentmore Rd, Calderwood NSW 2417<br>
      Tel: 0493 716 258<br>
      Email: info@harbourlanerealty.com.au</p>
    </div>
  </section>
</body>
</html>
```